Design some Business Cards

We are a contruction company.

We have our company registered logo. please see attached.

What we are after is 2 employers business cards.

Company: PW Trades Group (Handymen, Roofing, Carpentry)

Name: Dov Harriswick
Phone: 0483 560 214
Email: dov@[login to view URL]
Address: Harbourview NSW 2095

Instagram logo: @[login to view URL]
Facebook logo: @[login to view URL]

```html
<!DOCTYPE html>
<html lang="en">
<head>
<meta charset="utf-8">
<title>PW Trades Group – Business Cards</title>
<link href="https://fonts.googleapis.com/css2?family=Quicksand:wght@500;600;700&display=swap" rel="stylesheet">
<style>
  :root {
    --page: #e7e6ea;
    --card: #3a3446;
    --orange: #ef5a24;
    --white: #ffffff;
    --text-soft: #e4e2e8;
  }
  * { box-sizing: border-box; margin: 0; padding: 0; }
  html, body { width: 1200px; height: 900px; overflow: hidden; }
  body {
    background: var(--page);
    font-family: "Quicksand", sans-serif;
    position: relative;
  }
  .card {
    position: absolute;
    left: 260px;
    width: 680px;
    height: 390px;
    background: var(--card);
    border-radius: 6px;
    box-shadow: 0 10px 28px rgba(30, 25, 40, 0.25);
    overflow: hidden;
  }
  .card--front { top: 45px; }
  .card--back { top: 465px; }

  /* Company name */
  .brand {
    color: var(--white);
    font-weight: 600;
    white-space: nowrap;
  }
  .card--front .brand {
    position: absolute;
    left: 44px;
    top: 48px;
    font-size: 28px;
  }

  /* Contact block */
  .contact {
    position: absolute;
    right: 44px;
    top: 110px;
    text-align: right;
  }
  .contact__name {
    color: var(--white);
    font-weight: 700;
    font-size: 26px;
    display: flex;
    align-items: center;
    justify-content: flex-end;
    gap: 14px;
    margin-bottom: 26px;
  }
  .contact__row {
    color: var(--text-soft);
    font-weight: 500;
    font-size: 17px;
    display: flex;
    align-items: center;
    justify-content: flex-end;
    gap: 14px;
    margin-bottom: 10px;
  }
  .icon {
    width: 26px; height: 26px;
    flex: none;
  }

  /* Orange social bands */
  .bands {
    position: absolute;
    left: 0; bottom: 0;
    width: 680px; height: 60px;
  }
  .social {
    position: absolute;
    bottom: 12px;
    display: flex;
    align-items: center;
    gap: 10px;
    color: var(--white);
    font-weight: 600;
    font-size: 17px;
  }
  .social--left { left: 28px; }
  .social--right { right: 28px; }
  .social__circle {
    width: 20px; height: 20px; border-radius: 50%;
    border: 2px solid var(--white);
  }
  .social__square {
    width: 20px; height: 20px; border-radius: 4px;
    border: 2px solid var(--white);
  }

  /* Back */
  .card--back .brand {
    position: absolute;
    left: 0; right: 0; top: 135px;
    text-align: center;
    font-size: 40px;
  }
  .tagline {
    position: absolute;
    left: 0; right: 0; top: 215px;
    text-align: center;
    color: var(--white);
    font-weight: 600;
    font-size: 28px;
  }
</style>
</head>
<body>

<section class="card card--front">
  <p class="brand">PW Trades Group</p>

  <div class="contact">
    <p class="contact__name">Dov Harriswick
      <svg class="icon" viewBox="0 0 26 26" aria-hidden="true">
        <circle cx="13" cy="13" r="11.5" fill="none" stroke="var(--orange)" stroke-width="1.6"/>
        <circle cx="13" cy="10" r="3" fill="none" stroke="var(--orange)" stroke-width="1.6"/>
        <path d="M7.5 19c1-3 3-4.5 5.5-4.5s4.5 1.5 5.5 4.5" fill="none" stroke="var(--orange)" stroke-width="1.6"/>
      </svg>
    </p>
    <p class="contact__row">0483 560 214
      <svg class="icon" viewBox="0 0 26 26" aria-hidden="true">
        <circle cx="13" cy="13" r="11.5" fill="none" stroke="var(--orange)" stroke-width="1.6"/>
        <path d="M9 8.5l2.2-.6 1.3 3-1.4 1c.7 1.5 1.7 2.5 3.1 3.1l1-1.4 3 1.3-.6 2.2c-4.6.3-8.9-4-8.6-8.6z" fill="var(--orange)"/>
      </svg>
    </p>
    <p class="contact__row">dov@[login to view URL]
      <svg class="icon" viewBox="0 0 26 26" aria-hidden="true">
        <circle cx="13" cy="13" r="11.5" fill="none" stroke="var(--orange)" stroke-width="1.6"/>
        <rect x="7.5" y="9" width="11" height="8" rx="1" fill="none" stroke="var(--orange)" stroke-width="1.5"/>
        <path d="M7.5 9.5l5.5 4 5.5-4" fill="none" stroke="var(--orange)" stroke-width="1.5"/>
      </svg>
    </p>
    <p class="contact__row">Harbourview NSW 2095
      <svg class="icon" viewBox="0 0 26 26" aria-hidden="true">
        <circle cx="13" cy="13" r="11.5" fill="none" stroke="var(--orange)" stroke-width="1.6"/>
        <path d="M13 19.5s-4.5-4.6-4.5-7.8a4.5 4.5 0 0 1 9 0c0 3.2-4.5 7.8-4.5 7.8z" fill="none" stroke="var(--orange)" stroke-width="1.5"/>
        <circle cx="13" cy="11.7" r="1.6" fill="var(--orange)"/>
      </svg>
    </p>
  </div>

  <svg class="bands" viewBox="0 0 680 60" aria-hidden="true">
    <polygon points="0,8 250,8 280,60 0,60" fill="var(--orange)"/>
    <polygon points="330,16 680,16 680,60 355,60" fill="var(--orange)"/>
  </svg>
  <div class="social social--left">
    <span class="social__circle"></span>@pwtrades
  </div>
  <div class="social social--right">
    pwtrades<span class="social__square"></span>
  </div>
</section>

<section class="card card--back">
  <p class="brand">PW Trades Group</p>
  <p class="tagline">(Handymen, Roofing, Carpentry)</p>
</section>

</body>
</html>
```